Website Design for a Project Management Consulting Business

I have a logo design already and now I need a website.
I am a project manager and run my own consulting business.
Currently I am under contract with 3 major Kestrelmark 300 companies. I'd like a website I can direct current and future clients.
My job is running IT projects and working with developers to deliver business priorities.
The website should be professional and clean - I work IT projects and would like to incorporate that into any theme.
I'd like the site to have several page or breakoff links - sections would include : about me, about my services, a page to display all of my certification badges, another page to talk about highlights from past projects and so on.
Looking for a collaborative experience.

Industry/Entity Type

Kestrelmark 300 Consulting Firm - Project Management

Coding

Coded - Design and coding required

Number of Pages Required

1 page

Font styles to use
Serif

Colors
0094D4
00A9DD
6FCCEA
C7EBF8
E9F6FB
EE7325
F08F49
F5BC92
FAE3D3
FDF4ED

Requirements
Must have
• Sections that are a must: About Me (bio), About My Services, About my Certifications and Credentials, Experience on Past Projects,
Nice to have
• I have added the logo below - I'd like to use the logo and have it prominent ; should be professional and inviting

```html
<!DOCTYPE html>
<html lang="en">
<head>
<meta charset="utf-8">
<title>Keystone Delivery Partners</title>
<link href="https://fonts.googleapis.com/css2?family=Poppins:wght@400;500;600;700&display=swap" rel="stylesheet">
<style>
:root{
  --navy:#0a1d3d;
  --navy-2:#10305f;
  --blue:#1b6fd0;
  --blue-2:#2a86e6;
  --sky:#6fcbea;
  --ice:#e9f6fb;
  --grey:#eceef1;
  --ink:#1d2433;
  --muted:#5b6475;
  --white:#ffffff;
  --gold:#f2a81d;
}
*{box-sizing:border-box;margin:0;padding:0}
html,body{width:1200px;height:5076px;overflow:hidden}
body{font-family:'Poppins',sans-serif;color:var(--ink);background:var(--white);position:relative}
section,header,footer{position:absolute;left:0;width:1200px;overflow:hidden}
.abs{position:absolute}
.photo{position:absolute}

/* hero */
.hero{top:0;height:820px;background:linear-gradient(120deg,var(--navy) 0%,var(--navy-2) 55%,#1a4f93 100%)}
.topbar{top:0;left:0;width:1200px;height:34px;display:flex;align-items:center;justify-content:space-between;padding:0 110px 0 120px;color:#cfe0f5;font-size:13px;border-bottom:1px solid rgba(255,255,255,.12);z-index:3}
.topbar .right{display:flex;gap:26px;align-items:center}
.topbar .soc{display:flex;gap:8px}
.topbar .soc span{width:12px;height:12px;border-radius:50%;background:#cfe0f5;display:block}
.brand{left:120px;top:44px;display:flex;align-items:center;gap:10px;color:var(--white);z-index:3}
.brand .mark{width:40px;height:40px;border:2px solid var(--white)}
.brand b{font-size:17px;font-weight:600;line-height:1.15;letter-spacing:.5px}
.nav{right:110px;top:72px;display:flex;gap:30px;font-size:14px;color:var(--white);z-index:3}
.nav .on{color:var(--sky);border-bottom:2px solid var(--sky);padding-bottom:4px}
.hero h1{left:110px;top:290px;font-size:40px;line-height:1.25;font-weight:600;color:var(--white);width:460px;z-index:2}
.hero p{left:110px;top:400px;width:460px;font-size:14px;line-height:1.6;color:#c7d6ea;z-index:2}
.btn{display:inline-flex;align-items:center;gap:10px;background:var(--blue);color:var(--white);font-size:14px;font-weight:500;padding:12px 26px;border-radius:4px}
.btn i{width:16px;height:16px;border-radius:50%;background:var(--white);display:block}
.hero .btn{left:110px;top:545px;position:absolute;z-index:2}
.slide-ix{left:28px;top:300px;color:#9fb6d6;font-size:12px;line-height:1}
.slide-ix .bar{width:2px;height:260px;background:rgba(255,255,255,.25);margin:10px 0 10px 6px}
.hero-photo{left:560px;top:140px;width:360px;height:680px;background:linear-gradient(180deg,#3a5f8f,#16335e);border-radius:6px 6px 0 0;z-index:1}
.dots{left:110px;top:718px;display:flex;gap:8px;z-index:2}
.dots span{width:40px;height:4px;background:rgba(255,255,255,.35)}
.dots span:first-child{background:var(--white)}

/* about */
.about{top:820px;height:720px;background:var(--white)}
.about-backdrop{left:70px;top:150px;width:520px;height:450px;background:var(--ice)}
.about-photo{left:110px;top:130px;width:460px;height:460px;border-radius:50%;background:radial-gradient(circle at 50% 40%,#9fb3c8,#5f7a96);border:8px solid var(--white)}
.title{display:inline-block;font-size:34px;font-weight:600;color:var(--navy);padding:8px 16px;border-left:3px solid var(--blue);border-top:3px solid var(--blue)}
.about .title{position:absolute;left:645px;top:170px}
.about .copy{left:645px;top:258px;width:450px;font-size:13px;line-height:1.8;color:var(--muted)}
.about .copy p+p{margin-top:18px}
.btn-dark{background:var(--navy)}
.about .btn{position:absolute;left:680px;top:470px}

/* services */
.services{top:1540px;height:740px}
.services .band{left:0;top:0;width:1200px;height:740px}
.services .title{position:absolute;left:467px;top:115px;color:var(--white);border-color:var(--white);background:rgba(255,255,255,.08)}
.card{position:absolute;top:240px;width:300px;height:420px;background:var(--white);border-radius:12px;box-shadow:0 10px 30px rgba(0,0,0,.25);overflow:hidden}
.card .pic{margin:18px 18px 0;height:210px;border-radius:10px}
.card h3{font-size:16px;font-weight:600;color:var(--navy);margin:18px 20px 8px}
.card p{font-size:12px;line-height:1.6;color:var(--muted);margin:0 20px}
.card .go{position:absolute;right:0;bottom:0;width:70px;height:44px;background:var(--navy)}
.arrow-btn{position:absolute;width:40px;height:40px;border-radius:50%;border:2px solid var(--white)}

/* reviews */
.reviews{top:2280px;height:580px;background:var(--grey)}
.reviews .title{position:absolute;left:432px;top:100px}
.reviews .lede{left:280px;top:185px;width:640px;text-align:center;font-size:13px;line-height:1.7;color:var(--muted)}
.review{position:absolute;top:285px;width:308px;height:210px;background:var(--white);padding:22px 24px;box-shadow:0 4px 14px rgba(0,0,0,.08)}
.review .q{font-size:34px;font-weight:700;color:var(--navy);line-height:.8}
.review p{font-size:12px;line-height:1.6;color:var(--muted);margin-top:10px}
.review .who{position:absolute;left:24px;bottom:22px;display:flex;align-items:center;gap:10px;font-size:12px}
.review .who span{width:36px;height:36px;border-radius:50%;background:#c7a98c;display:block}
.dark-arrow{position:absolute;width:30px;height:30px;border-radius:50%;background:var(--navy)}

/* projects */
.projects{top:2860px;height:660px;background:var(--white)}
.projects .title{position:absolute;left:470px;top:112px}
.shot{position:absolute;top:220px;width:236px;height:280px}
.projects .btn{position:absolute;left:470px;top:545px}

/* certifications */
.certs{top:3520px;height:420px;background:linear-gradient(180deg,var(--grey),#f7f8fa)}
.certs .title{position:absolute;left:405px;top:85px}
.badge{position:absolute;top:200px;width:120px;height:120px;border-radius:50%;background:radial-gradient(circle,#ffc94a,var(--gold));border:6px solid #f8d27c}

/* contact */
.contact{top:3940px;height:620px;background:var(--white)}
.contact .title{position:absolute;left:468px;top:60px}
.field{position:absolute;height:56px;border:1px solid #d9dee6;background:var(--white);box-shadow:0 3px 8px rgba(0,0,0,.06);font-size:13px;color:var(--muted);padding:18px 16px}
.contact .btn{position:absolute;left:475px;top:500px;padding:14px 38px;font-weight:600}

/* footer */
.footer{top:4560px;height:516px;background:var(--navy);color:#c7d3e4}
.footer .col{position:absolute;top:140px;font-size:13px;line-height:2}
.footer h4{font-size:14px;font-weight:600;color:var(--white);margin-bottom:10px;letter-spacing:.5px}
.footer small{display:block;font-weight:600;color:var(--white);font-size:12px}
.sub{display:flex;align-items:center;justify-content:space-between;width:280px;height:38px;background:var(--white);border-radius:20px;padding:0 6px 0 16px;color:var(--muted);font-size:12px;margin-top:12px}
.sub i{width:28px;height:28px;border-radius:50%;background:var(--navy);display:block}
.f-soc{display:flex;gap:12px;margin-top:18px}
.f-soc span{width:38px;height:38px;border-radius:50%;border:2px solid #c7d3e4;display:block}
.legal{left:110px;top:470px;width:980px;display:flex;justify-content:space-between;font-size:12px;border-top:1px solid rgba(255,255,255,.15);padding-top:14px}
</style>
</head>
<body>

<header class="hero">
  <div class="topbar abs">
    <span>English</span>
    <div class="right">
      <span>Phone: +1 000 555 0142</span>
      <span>hello@keystonedelivery.example</span>
      <span>Login/Signup</span>
      <div class="soc"><span></span><span></span></div>
    </div>
  </div>
  <div class="brand abs"><div class="mark"></div><b>KEYSTONE<br>DELIVERY PARTNERS</b></div>
  <nav class="nav abs"><span class="on">Home</span><span>About Me</span><span>My Services</span><span>Certifications</span><span>Projects</span><span>Contact</span></nav>
  <div class="slide-ix abs">01<div class="bar"></div>04</div>
  <h1 class="abs">Keystone Delivery Partners</h1>
  <p class="abs">Steady delivery for complex technology programs, aligning developers, stakeholders and business priorities so every release lands on time and on budget.</p>
  <span class="btn">Get Started <i></i></span>
  <div class="photo hero-photo" role="img" aria-label="Portrait of a consultant in a dark suit with arms crossed"></div>
  <div class="dots abs"><span></span><span></span><span></span></div>
</header>

<section class="about">
  <div class="abs about-backdrop"></div>
  <div class="photo about-photo" role="img" aria-label="Portrait of a smiling project manager in a blue shirt"></div>
  <h2 class="title">About Me</h2>
  <div class="copy abs">
    <p>Dorian Vale is the owner of Keystone Delivery Partners LLC and serves as principal lead consultant on waterfall and agile contract opportunities.</p>
    <p>Keystone Delivery Partners LLC has engaged in contract roles with Kestrelmark 300 companies across various industries including banking and credit unions, global supply chain and international food distribution. Dorian brings 15 years of experience to his clients and engagements.</p>
  </div>
  <span class="btn btn-dark">Read More <i></i></span>
</section>

<section class="services">
  <svg class="abs band" width="1200" height="740" viewBox="0 0 1200 740" aria-hidden="true">
    <defs><linearGradient id="svcg" x1="0" y1="0" x2="1" y2="1"><stop offset="0" stop-color="#2a86e6"/><stop offset="1" stop-color="#1b5fb8"/></linearGradient></defs>
    <polygon points="0,40 1200,0 1200,700 0,740" fill="url(#svcg)"/>
    <polygon points="700,0 1200,0 1200,40" fill="#0a1d3d"/>
    <polygon points="0,700 500,740 0,740" fill="#0a1d3d"/>
  </svg>
  <h2 class="title">My Services</h2>
  <span class="arrow-btn" style="left:40px;top:430px"></span>
  <div class="card" style="left:120px">
    <div class="pic" role="img" aria-label="Team working at laptops in an office" style="background:linear-gradient(135deg,#c9d6e2,#7f95ab)"></div>
    <h3>IT Projects</h3>
    <p>Planning and delivering technology programs with developer teams from kickoff through release.</p>
    <span class="go"></span>
  </div>
  <div class="card" style="left:450px">
    <div class="pic" role="img" aria-label="Consultants meeting around a conference table" style="background:linear-gradient(135deg,#d8cfc4,#8a7d70)"></div>
    <h3>Consulting</h3>
    <p>Guidance on roadmaps, governance and delivery methods tailored to each business priority.</p>
    <span class="go"></span>
  </div>
  <div class="card" style="left:780px">
    <div class="pic" role="img" aria-label="Hands reviewing financial reports with a calculator" style="background:linear-gradient(135deg,#c4ccd8,#6d7b91)"></div>
    <h3>Audit &amp; Assurance</h3>
    <p>Independent project health checks, risk reviews and controls to keep programs on track.</p>
    <span class="go"></span>
  </div>
  <span class="arrow-btn" style="left:1120px;top:430px"></span>
</section>

<section class="reviews">
  <h2 class="title">Client Reviews</h2>
  <p class="lede abs">Feedback from leaders and delivery teams who partnered with us on demanding programs across banking, supply chain and distribution.</p>
  <span class="dark-arrow" style="left:60px;top:375px"></span>
  <div class="review" style="left:110px">
    <div class="q">“</div>
    <p>Clear plans, honest status reports and a calm hand when priorities shifted. Our release landed ahead of schedule.</p>
    <div class="who"><span role="img" aria-label="Reviewer avatar"></span>Wren Castellan</div>
  </div>
  <div class="review" style="left:446px">
    <div class="q">“</div>
    <p>Dorian bridged our business and developer teams with ease and kept every stakeholder informed from start to finish.</p>
    <div class="who"><span role="img" aria-label="Reviewer avatar"></span>Wren Castellan</div>
  </div>
  <div class="review" style="left:782px">
    <div class="q">“</div>
    <p>A structured, practical approach to risk and scope that turned a stalled migration into a confident, successful launch.</p>
    <div class="who"><span role="img" aria-label="Reviewer avatar"></span>Wren Castellan</div>
  </div>
  <span class="dark-arrow" style="left:1110px;top:375px"></span>
</section>

<section class="projects">
  <h2 class="title">Past Projects</h2>
  <div class="shot" role="img" aria-label="Developers collaborating at a desk" style="left:110px;background:linear-gradient(135deg,#b8cbe0,#5a7799)"></div>
  <div class="shot" role="img" aria-label="Colleagues reviewing a laptop together" style="left:358px;background:linear-gradient(135deg,#c6d3df,#4e6a85)"></div>
  <div class="shot" role="img" aria-label="Team meeting in a bright conference room" style="left:606px;background:linear-gradient(135deg,#d6cdbf,#7c6f60)"></div>
  <div class="shot" role="img" aria-label="Engineers discussing work at a monitor" style="left:854px;background:linear-gradient(135deg,#bcc9d6,#56708b)"></div>
  <span class="btn btn-dark">View More Projects <i></i></span>
</section>

<section class="certs">
  <h2 class="title">My Certifications</h2>
  <div class="badge" style="left:350px"></div>
  <div class="badge" style="left:540px"></div>
  <div class="badge" style="left:730px"></div>
</section>

<section class="contact">
  <h2 class="title">Contact Me</h2>
  <div class="field" style="left:220px;top:160px;width:382px">First Name</div>
  <div class="field" style="left:618px;top:160px;width:382px">Last Name</div>
  <div class="field" style="left:220px;top:240px;width:780px">Email Address</div>
  <div class="field" style="left:220px;top:320px;width:780px">Subject</div>
  <div class="field" style="left:220px;top:400px;width:780px;height:112px">Message</div>
  <span class="btn">SUBMIT NOW <i></i></span>
</section>

<footer class="footer">
  <svg class="abs" style="left:0;top:0" width="1200" height="60" viewBox="0 0 1200 60" aria-hidden="true">
    <polygon points="0,0 1200,0 1200,10 0,50" fill="#ffffff"/>
    <polygon points="700,18 1200,10 1200,28" fill="#1b6fd0"/>
  </svg>
  <div class="col" style="left:110px"><h4>QUICK LINKS</h4>Home<br>About Me<br>My Services<br>My Certifications<br>Past Projects<br>Contact Us</div>
  <div class="col" style="left:300px"><h4>SERVICES</h4>IT Projects<br>Consulting<br>Audit &amp; Assurance</div>
  <div class="col" style="left:510px;width:240px;line-height:1.6"><h4>CONTACT US</h4><small>ADDRESS</small>210 Harbor Row, Suite 4,<br>Lakemont<br><br><small>PHONE</small>+1 000 555 0142<br><br><small>EMAIL</small>hello@keystonedelivery.example</div>
  <div class="col" style="left:810px;width:290px;line-height:1.6"><h4>NEWSLETTER</h4>Monthly notes on delivery, planning and leading technology teams.
    <div class="sub">Enter Email <i></i></div>
    <div class="f-soc"><span></span><span></span><span></span></div>
  </div>
  <div class="legal abs"><span>© 2020 KEYSTONE DELIVERY PARTNERS All Rights Reserved</span><span>Terms of use | Privacy Policy</span></div>
</footer>

</body>
</html>
```